Cutting Edge Cloud Hosting Provider needs business card design

We are a new Cloud Hosting Provider called Velkaro Hosting. (Velkaro means cloudy in Spanish.) We provide clients with virtual resources and not virtual machines directly. Our clients purchase the resources that they will use (RAM,CPU, Hard drive space) then use those resources in as many virtual machines as they like.

We are looking for a business card design that is cutting edge and hip.
Updates

The name of the company is "Velkaro Hosting". Please include the "Hosting" part of our name in the design.

Thanks

Target Market(s)

21-35 developers and I.T. Staff

Industry/Entity Type

Business

Requirements
Must have
• Rounded corners, Must Incorporate our logo, individual's name must be prominent

```html
<!DOCTYPE html>
<html lang="en">
<head>
<meta charset="utf-8">
<title>Velkaro Hosting — Business Card</title>
<link rel="stylesheet" href="https://fonts.googleapis.com/css2?family=Comfortaa:wght@400;600;700&display=swap">
<style>
  :root {
    --backdrop: #34507f;
    --ink-deep: #2b3e6c;
    --ink-mid: #4a68a0;
    --sky-top: #6783b8;
    --sky-mid: #b9c9e6;
    --paper-top: #f6f8fc;
    --paper-bottom: #dde5f2;
  }
  * { box-sizing: border-box; margin: 0; padding: 0; }
  html, body {
    width: 1200px;
    height: 900px;
    overflow: hidden;
    background: var(--backdrop);
    font-family: "Comfortaa", sans-serif;
  }
  .sheet {
    position: relative;
    width: 1200px;
    height: 900px;
  }
  .card {
    position: absolute;
    top: 300px;
    width: 533px;
    height: 300px;
    border-radius: 22px;
    overflow: hidden;
    background: linear-gradient(180deg, var(--paper-top) 0%, var(--paper-bottom) 100%);
    box-shadow: 0 8px 18px rgba(10, 25, 55, 0.45);
  }
  .card--front { left: 45px; }
  .card--back { left: 622px; }
  .card__sky {
    position: absolute;
    left: 0; right: 0; top: 0;
    height: 115px;
    background: linear-gradient(180deg, var(--sky-top) 0%, var(--sky-mid) 55%, rgba(246, 248, 252, 0) 100%);
  }
  .card__content {
    position: absolute;
    inset: 0;
    text-align: center;
    color: var(--ink-deep);
  }
  .wordmark {
    position: absolute;
    left: 0; right: 0;
    top: 96px;
    font-size: 104px;
    font-weight: 700;
    letter-spacing: 1px;
    line-height: 1;
    color: var(--ink-deep);
  }
  .tagline {
    position: absolute;
    left: 0; right: 0;
    top: 212px;
    font-size: 32px;
    font-weight: 600;
    color: var(--ink-mid);
  }
  .person-name {
    position: absolute;
    left: 0; right: 0;
    top: 120px;
    font-size: 60px;
    font-weight: 600;
    line-height: 1;
  }
  .person-role {
    position: absolute;
    left: 0; right: 0;
    top: 186px;
    font-size: 22px;
    font-weight: 700;
  }
  .contact {
    position: absolute;
    left: 0; right: 0;
    top: 218px;
    list-style: none;
    color: var(--ink-mid);
    font-weight: 600;
  }
  .contact__email { font-size: 18px; line-height: 22px; }
  .contact__phone { font-size: 15px; line-height: 19px; }
</style>
</head>
<body>
<main class="sheet">

  <section class="card card--front" aria-label="Card front">
    <div class="card__sky" role="img" aria-label="Cloud illustration along the top edge of the card"></div>
    <div class="card__content">
      <p class="wordmark">velkaro</p>
      <p class="tagline">cloud hosting</p>
    </div>
  </section>

  <section class="card card--back" aria-label="Card back">
    <div class="card__sky" role="img" aria-label="Cloud illustration along the top edge of the card"></div>
    <div class="card__content">
      <h1 class="person-name">dana voss</h1>
      <p class="person-role">vice president</p>
      <ul class="contact">
        <li class="contact__email">dana (at) velkaro.com</li>
        <li class="contact__phone">p: 555 · 014 · 2730</li>
        <li class="contact__phone">c: 555 · 019 · 4481</li>
      </ul>
    </div>
  </section>

</main>
</body>
</html>
```